Resume design

I am a nonprofit director looking to update my resume. My job entails positioning our organization as a leader in new communications, and I want something that reflects this - meaning it is a little crisper than what is offered by the standard resume service.
I have some examples of the type of aesthetic I'm looking for: lots of white space/breathing room, clean fonts, and a pop of color. That said, I'm not looking to create some fantastically re-envisioned version of the resume. I need to follow the general format but in a way that is elegant and sharp.
Industry/Entity Type
Communications
Requirements
Must have
- The majority of the text that I will provide (although I am open to suggestions and adjustments)
But keep to two pages. I'm open to suggestions for how to massage or shorten the text to do this.
Nice to have
- a few pops of color - esp. orange, Tiffany blue, or open to other suggestions - needs to feel fresh and cutting edge
prefer sans serif font but open to ideas
Should not have
- no photos
no artwork unless you have a suggestion for something that feels right
no tilted text
no pastel colors, and prefer to stay away from earth tones unless offset by a bolder color

```html
<!DOCTYPE html>
<html lang="en">
<head>
<meta charset="utf-8">
<title>Resume – Page Two</title>
<link rel="stylesheet" href="https://fonts.googleapis.com/css2?family=Montserrat:wght@600;700&family=Source+Sans+3:ital,wght@0,400;0,500;1,400&display=swap">
<style>
  :root {
    --teal: #1ab39a;
    --teal-line: #8fd8cb;
    --ink: #111111;
    --paper: #ffffff;
  }
  * { box-sizing: border-box; margin: 0; padding: 0; }
  html, body { width: 942px; height: 1200px; overflow: hidden; background: var(--paper); }
  body { font-family: "Source Sans 3", "Myriad Pro", Arial, sans-serif; color: var(--ink); font-size: 14.5px; line-height: 18px; }
  .page { position: relative; width: 942px; height: 1200px; background: var(--paper); }
  .spine { position: absolute; left: 201px; top: 0; width: 1px; height: 1200px; background: var(--teal-line); }
  .band {
    position: absolute; left: 201px; right: 0; height: 37px;
    background: var(--teal); color: #fff;
    font-family: "Montserrat", Arial, sans-serif; font-weight: 700;
    font-size: 19px; letter-spacing: 0.6px; line-height: 37px; padding-left: 13px;
  }
  .band--footer { top: 1148px; height: 52px; }
  .block { position: absolute; left: 201px; right: 20px; }
  .block--quotes { right: 50px; }
  .item { position: relative; padding-left: 10px; }
  .item::before { content: "-"; position: absolute; left: 0; color: var(--teal); }
  .item--plain::before { content: none; }
  .employer { color: var(--teal); margin-top: 6px; }
  .employer:first-child { margin-top: 0; }
  .role { padding-left: 10px; }
  .role .dates { font-style: italic; font-size: 13.5px; }
  .role .sep { display: inline-block; margin: 0 13px 0 14px; }
  .strong { font-weight: 500; }
  .note { color: var(--teal); font-style: italic; font-size: 13.5px; }
  .link { color: var(--teal); }
  .lead-row { display: flex; line-height: 19.5px; }
  .lead-row .dates { width: 100px; flex: none; color: var(--teal); font-style: italic; }
  .rule { position: absolute; left: 201px; right: 0; top: 898px; height: 1px; background: var(--teal-line); }
  .quote { margin-bottom: 9px; padding-left: 13px; font-style: italic; font-size: 14px; line-height: 18px; }
  .quote .words { color: var(--teal); }
  .quote .source { color: var(--ink); }
</style>
</head>
<body>
<main class="page">
  <div class="spine"></div>

  <h2 class="band" style="top:28px">CAREER CHRONOLOGY</h2>
  <section class="block" style="top:83px">
    <div class="item employer">Coastal Environmental Alliance, Santa Barbara, CA</div>
    <div class="role"><span class="dates">2006 – Present</span><span class="sep">·</span>Assistant Director</div>
    <div class="role"><span class="dates">2004 – 2006</span><span class="sep">·</span>Community Relations Director</div>
    <div class="role"><span class="dates">1996 – 2004</span><span class="sep">·</span>Communications Director</div>
    <div class="role"><span class="dates">1995 – 1996</span><span class="sep">·</span>Communications Associate</div>
    <div class="item employer">Harbor Seasons Magazine, Santa Barbara, CA</div>
    <div class="role"><span class="dates">2011 – Present</span><span class="sep">·</span>Sustainabilty Editor</div>
    <div class="item employer">Coalition for Energy Savings, Washington, D.C.</div>
    <div class="role"><span class="dates">1993 – 1995</span><span class="sep">·</span>Communications Associate</div>
    <div class="item employer">Wild Lands Federation, Washington, D.C.</div>
    <div class="role"><span class="dates">1992 – 1993</span><span class="sep">·</span>Communications Associate</div>
  </section>

  <h2 class="band" style="top:318px">EDUCATION</h2>
  <section class="block" style="top:373px">
    <div class="item"><span class="strong">Master of Arts in Communication Design</span>, Chesapeake University, Baltimore, Maryland</div>
    <div class="item"><span class="strong">Bachelor of Science in Journalism</span>, Cascade State University, Eugene, Oregon</div>
  </section>

  <h2 class="band" style="top:427px">TECHNICAL PROFICIENCIES</h2>
  <section class="block" style="top:481px">
    <div class="item">Quill Office (Writer, Ledger, Deck, Inbox); PostPigeon, Campfire Boards, DonorGrid</div>
  </section>

  <h2 class="band" style="top:515px">SAMPLE PUBLICATIONS</h2>
  <section class="block" style="top:569px">
    <div class="item item--plain">Author and/or editor of dozens of technical reports and advocacy papers, including:</div>
    <div class="item">Charting Clean Power: A Regional Roadmap for the Central Coast <span class="link">http://www.coastalea.org/publications</span> <span class="note">(strategy report)</span></div>
    <div class="item">Does the Coast Really Need New Gas Terminals? <span class="link">http://www.coastalea.org/publications</span> <span class="note">(policy paper)</span></div>
    <div class="item">Rooftop Power on the Central Coast: Practical Steps for Clearing Obstacles<br><span class="link">http://www.coastalea.org/publications</span> <span class="note">(strategy report)</span></div>
    <div class="item">Healthy Spaces for Kids <span class="note">(survey brief and final report)</span></div>
    <div class="item">Waste Conversion Methods and Resource Planning for a Modern Region <span class="note">(technical paper)</span></div>
    <div class="item">Rethinking the Landfill: Managing Resources for the Decades Ahead <span class="note">(policy paper)</span></div>
  </section>

  <h2 class="band" style="top:730px">COMMUNITY LEADERSHIP</h2>
  <section class="block" style="top:784px">
    <div class="item lead-row"><span class="dates">2013 to Present</span><span><span class="strong">Board Member,</span> Rising From Within, Santa Barbara, CA</span></div>
    <div class="item lead-row"><span class="dates">2011 to Present</span><span><span class="strong">Alumni Committee Chair,</span> Brave Leaders Program, Santa Barbara, CA</span></div>
    <div class="item lead-row"><span class="dates">2009-2010</span><span><span class="strong">Participant,</span> Brave Leaders Program, Santa Barbara, CA</span></div>
    <div class="item lead-row"><span class="dates">2009-2012</span><span><span class="strong">Planning Committee Member,</span> Alliance for Excellence, Santa Barbara, CA</span></div>
    <div class="item lead-row"><span class="dates">2011</span><span><span class="strong">Participant,</span> Pacific Social Innovation Journal: Non-Profit Management Institute, Santa Barbara, CA</span></div>
  </section>

  <div class="rule"></div>
  <section class="block block--quotes" style="top:915px">
    <p class="quote"><span class="words">“Marin is the hub that makes the wheels of big projects run smoothly. Her leadership, delegation and motivational skills are exceptional.”</span> <span class="source">·&nbsp; Dana Whitfield, Santa Barbara Mayor</span></p>
    <p class="quote"><span class="words">“Anytime I have the opportunity to work with a team that Marin puts together, I know I’ll absolutely love each person she has hand selected. She’s brought together people of all walks throughout the community to pull off professional large-scale events on non-profit budgets.”</span> <span class="source">·&nbsp; Owen Marsh, CEO, Dreamwave / Dreamwave Records</span></p>
    <p class="quote"><span class="words">“Marin emerged as a leader among leaders in our Brave Leaders program for experienced nonprofit executives.”</span><br><span class="source">·&nbsp; Paul Renner, President &amp; Board Chair at Rising From Within</span></p>
  </section>

  <div class="band band--footer"></div>
</main>
</body>
</html>
```